custom carpentry, woodworking and home repair company needs logo design and business card design

Attention: I apologize but I just received notification from my state that I cannot use the company name that I originally submitted (Beyond The Bench). The new name will be Joinolux We need a company logo and business card design for our new company based in the Hampton Roads area of Virginia. The company name is Joinolux. The final design should give a first impression of true craftsmanship and attention to detail. We would like the card to include the company name, my name Mark Tellman (owner), phone number (757) 348-2615, website (joinolux-example.com) and email address (mark@joinolux-example.com). Everything else is up to your discretion. Thanks, have fun, and good luck.

Industry/Entity Type

Business

Contact Information for Business Card

See project description

Logo Text

see project description

Colors

Designer to choose colors to be used in the design.

```html
<!DOCTYPE html>
<html lang="en">
<head>
<meta charset="UTF-8">
<title>Joinolux Business Card</title>
<link href="https://fonts.googleapis.com/css2?family=Montserrat:wght@600&family=Open+Sans:wght@400;600&display=swap" rel="stylesheet">
<style>
  :root {
    --backdrop: #ecebe8;
    --card-dark: #050505;
    --card-light: #ffffff;
    --amber: #d98e1c;
    --ink: #2b2b2b;
    --ink-soft: #555555;
    --on-dark: #ffffff;
  }
  * { margin: 0; padding: 0; box-sizing: border-box; }
  html, body {
    width: 1200px; height: 900px; overflow: hidden;
    background: var(--backdrop);
  }
  .sheet {
    position: relative; width: 1200px; height: 900px;
    display: flex; align-items: center; justify-content: center; gap: 40px;
  }
  .card {
    width: 520px; height: 297px; position: relative;
    box-shadow: 0 6px 18px rgba(0,0,0,0.15);
  }
  .card--front {
    background: var(--card-dark);
    display: flex; flex-direction: column; align-items: center; justify-content: center; gap: 16px;
  }
  .brand-dot {
    width: 56px; height: 56px; border-radius: 50%;
    background: var(--amber);
  }
  .brand-name {
    font-family: "Montserrat", sans-serif; font-weight: 600;
    font-size: 38px; letter-spacing: 1px; text-transform: uppercase;
    color: var(--on-dark); line-height: 1;
  }
  .card--back { background: var(--card-light); }
  .back-brand {
    position: absolute; left: 30px; top: 0; width: 250px; height: 100%;
    display: flex; flex-direction: column; align-items: center; justify-content: center; gap: 14px;
  }
  .back-brand .brand-dot { width: 90px; height: 90px; }
  .back-brand .brand-name { color: var(--amber); font-size: 30px; }
  .divider {
    position: absolute; left: 300px; top: 38px; width: 1.5px; height: 150px;
    background: var(--amber);
  }
  .contact {
    position: absolute; left: 318px; top: 40px;
    font-family: "Open Sans", sans-serif;
  }
  .contact__name {
    font-weight: 600; font-size: 16px; color: var(--amber);
    text-transform: uppercase; letter-spacing: 0.3px;
  }
  .contact__role { font-size: 12px; color: var(--ink-soft); margin-bottom: 16px; }
  .contact__list { list-style: none; }
  .contact__item {
    display: flex; align-items: center; gap: 7px;
    font-size: 11.5px; color: var(--ink); line-height: 19px;
  }
  .contact__item svg { width: 10px; height: 10px; flex: none; fill: var(--amber); }
  .contact__region { font-size: 12.5px; color: var(--ink); margin-top: 12px; }
</style>
</head>
<body>
<main class="sheet">
  <section class="card card--front" aria-label="Card front">
    <span class="brand-dot"></span>
    <span class="brand-name">Joinolux</span>
  </section>

  <section class="card card--back" aria-label="Card back">
    <div class="back-brand">
      <span class="brand-dot"></span>
      <span class="brand-name">Joinolux</span>
    </div>
    <div class="divider"></div>
    <div class="contact">
      <p class="contact__name">Mark Tellman</p>
      <p class="contact__role">Owner</p>
      <ul class="contact__list">
        <li class="contact__item">
          <svg viewBox="0 0 10 10"><path d="M2 0.5 L3.6 2.6 L2.8 3.6 C3.4 5 5 6.6 6.4 7.2 L7.4 6.4 L9.5 8 L8.4 9.5 C4.5 9 1 5.5 0.5 1.6 Z"/></svg>
          (757) 348-2615
        </li>
        <li class="contact__item">
          <svg viewBox="0 0 10 10"><path d="M0 2 H10 V8.5 H0 Z M0.6 2.6 L5 5.8 L9.4 2.6" stroke="#fff" stroke-width="0.8"/></svg>
          mark@joinolux-example.com
        </li>
        <li class="contact__item">
          <svg viewBox="0 0 10 10"><circle cx="5" cy="5" r="4.8"/></svg>
          www.joinolux-example.com
        </li>
      </ul>
      <p class="contact__region">Cedar Harbor, Virginia</p>
    </div>
  </section>
</main>
</body>
</html>
```